Business card for home decor store and design

I need a business card for my home decor boutique that’s professional looking boho/rustic. We sell vintage furniture, vintage finds, lamps, throws, rugs. We also carry a Diy paint line for refinishing furniture. We offer workshop on painting furniture, private or group setting. We in the heart of Old Town Red Bluff. We love to design, build and restore. Family owned small business. Our style is rustic boho farmhouse. We search for one of a kind found and repurposed items. We love vintage home decor, vintage windows.

Target Market(s)

Home decor

Industry/Entity Type

Home Accessories

Contact Information for Business Card

Have a rustic look/boho

Font styles to use
Serif
Script

Requirements
Must have
• Logo

```html
<!DOCTYPE html>
<html lang="en">
<head>
<meta charset="utf-8">
<title>Hollow &amp; Hearth Co. — Business Card</title>
<link rel="stylesheet" href="https://fonts.googleapis.com/css2?family=Montserrat:wght@400;500;600;700&display=swap">
<style>
  :root {
    --backdrop: #b4b4b4;
    --ink: #0d0d0d;
    --paper-white: #ffffff;
    --wood-light: #f1d6b8;
    --wood-mid: #e6c39c;
    --wood-warm: #dcb18a;
    --band: #000000;
  }
  * { box-sizing: border-box; margin: 0; padding: 0; }
  html, body { width: 1200px; height: 1200px; overflow: hidden; }
  body {
    position: relative;
    background: var(--backdrop);
    font-family: "Montserrat", sans-serif;
    color: var(--ink);
  }
  .card {
    position: absolute;
    left: 246px;
    width: 677px;
    height: 386px;
    border-radius: 37px;
    overflow: hidden;
  }
  .card--front { top: 181px; }
  .card--back { top: 658px; }
  .card__wood {
    position: absolute;
    inset: 0;
    background:
      linear-gradient(180deg, rgba(255,255,255,0.10) 0%, rgba(0,0,0,0) 40%, rgba(120,70,30,0.06) 100%),
      linear-gradient(90deg, var(--wood-light) 0%, var(--wood-mid) 35%, var(--wood-light) 60%, var(--wood-warm) 100%);
  }
  .card__band {
    position: absolute;
    left: 0; right: 0; bottom: 0;
    height: 61px;
    background: var(--band);
    color: var(--paper-white);
    font-size: 24px;
    font-weight: 400;
  }
  .band-item {
    position: absolute;
    top: 14px;
    transform: translateX(-50%);
    white-space: nowrap;
    letter-spacing: 0.3px;
  }
  .brand-seal {
    position: absolute;
    border: 3px solid var(--ink);
    border-radius: 50%;
  }
  .brand-name {
    position: absolute;
    transform: translate(-50%, -50%);
    white-space: nowrap;
    font-weight: 700;
    color: var(--ink);
  }
  .front-brand-seal { left: 38px; top: 68px; width: 212px; height: 212px; }
  .front-brand-name { left: 144px; top: 174px; font-size: 16px; }
  .back-brand-seal { left: 278px; top: 18px; width: 120px; height: 120px; border-width: 2px; }
  .back-brand-name { left: 338px; top: 78px; font-size: 9.5px; }

  .person-name {
    position: absolute;
    left: 296px; top: 74px;
    font-size: 37px;
    font-weight: 700;
    letter-spacing: 0.4px;
    white-space: nowrap;
  }
  .person-title {
    position: absolute;
    left: 456px; top: 122px;
    transform: translateX(-50%);
    font-size: 24px;
    font-weight: 400;
    white-space: nowrap;
  }
  .rule { position: absolute; }
  .front-rule { left: 296px; top: 157px; }
  .back-rule { left: 90px; top: 217px; }

  .contact {
    position: absolute;
    left: 297px;
    display: flex;
    align-items: center;
    gap: 6px;
    font-size: 21px;
    font-weight: 600;
    white-space: nowrap;
  }
  .contact--phone { top: 199px; }
  .contact--email { top: 236px; }
  .contact__icon { width: 27px; height: 27px; flex: none; }

  .offer {
    position: absolute;
    left: 0; right: 0;
    text-align: center;
    font-size: 24px;
    line-height: 26px;
    font-weight: 400;
  }
  .offer strong { font-weight: 700; }
  .offer--sell { top: 157px; }
  .offer--workshop { top: 230px; }
</style>
</head>
<body>

  <section class="card card--front">
    <div class="card__wood" role="img" aria-label="Light maple butcher-block wood grain background"></div>

    <div class="brand-seal front-brand-seal"></div>
    <div class="brand-name front-brand-name">Hollow &amp; Hearth Co.</div>

    <h1 class="person-name">Marla Vennick</h1>
    <p class="person-title">Owner and Founder</p>

    <svg class="rule front-rule" width="340" height="10" viewBox="0 0 340 10">
      <line x1="5" y1="5" x2="335" y2="5" stroke="#0d0d0d" stroke-width="2"/>
      <circle cx="5" cy="5" r="4" fill="#0d0d0d"/>
      <circle cx="335" cy="5" r="4" fill="#0d0d0d"/>
    </svg>

    <div class="contact contact--phone">
      <svg class="contact__icon" viewBox="0 0 28 28">
        <circle cx="14" cy="14" r="14" fill="#0d0d0d"/>
        <path d="M10.2 7.5c.6-.3 1.2 0 1.5.5l1.3 2.5c.3.6.1 1.2-.4 1.6l-1 .7c.7 1.6 1.9 2.9 3.5 3.7l.8-1c.4-.5 1-.6 1.6-.3l2.4 1.4c.5.3.7 1 .4 1.6-.7 1.5-2.1 2.3-3.6 2-4.3-.9-7.7-4.4-8.5-8.8-.2-1.6.7-3.2 2-3.9z" fill="#ffffff"/>
      </svg>
      <span>+1 555-014-2290</span>
    </div>
    <div class="contact contact--email">
      <svg class="contact__icon" viewBox="0 0 28 28">
        <circle cx="14" cy="14" r="14" fill="#0d0d0d"/>
        <rect x="7" y="9" width="14" height="10" rx="1" fill="#ffffff"/>
        <path d="M7.5 9.5 14 14.8 20.5 9.5" fill="none" stroke="#0d0d0d" stroke-width="1.3"/>
      </svg>
      <span>hollowhearth@mailbox.com</span>
    </div>

    <div class="card__band">
      <span class="band-item" style="left:148px">Home decor</span>
      <span class="band-item" style="left:247px">|</span>
      <span class="band-item" style="left:325px">Furniture</span>
      <span class="band-item" style="left:404px">|</span>
      <span class="band-item" style="left:515px">Antiques shop</span>
    </div>
  </section>

  <section class="card card--back">
    <div class="card__wood" role="img" aria-label="Light maple butcher-block wood grain background"></div>

    <div class="brand-seal back-brand-seal"></div>
    <div class="brand-name back-brand-name">Hollow &amp; Hearth Co.</div>

    <p class="offer offer--sell"><strong>We sell</strong> vintage furniture,<br>vintage finds, lamps, throws, rugs.</p>

    <svg class="rule back-rule" width="497" height="10" viewBox="0 0 497 10">
      <line x1="5" y1="5" x2="492" y2="5" stroke="#0d0d0d" stroke-width="2"/>
      <circle cx="5" cy="5" r="4" fill="#0d0d0d"/>
      <circle cx="492" cy="5" r="4" fill="#0d0d0d"/>
    </svg>

    <p class="offer offer--workshop"><strong>We offer</strong> workshop on painting furniture,<br>private or group setting.</p>

    <div class="card__band">
      <span class="band-item" style="left:148px">Home decor</span>
      <span class="band-item" style="left:247px">|</span>
      <span class="band-item" style="left:325px">Furniture</span>
      <span class="band-item" style="left:404px">|</span>
      <span class="band-item" style="left:515px">Antiques shop</span>
    </div>
  </section>

</body>
</html>
```